Sonoma County Winery needs a fresh label design for new line of natural wines

The growing natural wine market requires a fresh perspective. Traditional wine labels don't attract the attention of natural wine buyers or the spirit for which they were made. Natural wines tend to be sustainable, organic and biodynamic. Natural wines also break norms and have disrupted the commercial wine industry with their non-traditional imagery and label designs. Natural wines stick out on the shelf for their brighter colors, illustrations and more handwritten font selections. Bottles are typically flint (clear glass) showing the true color of the wine, red and white. Red wines are typically not opaque, but rather light colored with zero filtration (
see attached pic). No capsule is used, therefore, the cork is shown through the glass bottle.

Target Market(s)

Wine buyers between the ages of 21-35 generally living in large cities, but more specifically San Francisco and Los Angeles

Requirements
Must have
• Dimensions:2 3/4 Inches Wide5 1/4 Inches TallIntended to print on Bright White Felt paper CMYK
Nice to have
• It may not have any words on the front label at all. It's more about symbolism and color and design then it is about the actual brand name (which will go on the back where all the legal stuff is). I've included several bottle shots from natural winemakers that may give you a sense that there is no one way to design a natural wine label, but rather several directions at this early stage in the market cycle
Should not have
• If it looks and smells like a traditional wine label, it's probably not the right idea

```html
<!DOCTYPE html>
<html lang="en">
<head>
<meta charset="UTF-8">
<title>Lorem Ipsum — Natural Wine Label</title>
<link href="https://fonts.googleapis.com/css2?family=Amatic+SC:wght@700&family=Caveat:wght@500&display=swap" rel="stylesheet">
<style>
  :root {
    --backdrop: #b98585;
    --label-paper: #f1ece7;
    --ink-navy: #1b2456;
    --hill-pink: #eaa6a8;
    --hill-rose: #d9979f;
    --hill-mauve: #a17bac;
    --hill-violet: #7066ad;
    --hill-blue: #4f57a3;
    --hill-deep: #2f3b8d;
    --volume-mark: #e4e2f1;
  }
  * { margin: 0; padding: 0; box-sizing: border-box; }
  html, body {
    width: 960px;
    height: 1200px;
    overflow: hidden;
    background: var(--backdrop);
  }
  .canvas {
    position: relative;
    width: 960px;
    height: 1200px;
    background: var(--backdrop);
  }
  .wine-label {
    position: absolute;
    left: 180px;
    top: 160px;
    width: 600px;
    height: 880px;
    background: var(--label-paper);
    overflow: hidden;
  }
  .label-header {
    position: absolute;
    top: 0;
    left: 0;
    width: 100%;
    height: 275px;
    text-align: center;
  }
  .brand-name {
    position: absolute;
    top: 58px;
    width: 100%;
    font-family: "Amatic SC", cursive;
    font-weight: 700;
    font-size: 118px;
    line-height: 1;
    letter-spacing: 2px;
    color: var(--ink-navy);
  }
  .tagline {
    position: absolute;
    top: 196px;
    width: 100%;
    font-family: "Caveat", cursive;
    font-weight: 500;
    font-size: 30px;
    line-height: 1;
    color: var(--ink-navy);
  }
  .landscape {
    position: absolute;
    left: 0;
    top: 275px;
    width: 100%;
    height: 605px;
    background: linear-gradient(
      to bottom,
      var(--hill-pink) 0%,
      var(--hill-rose) 18%,
      var(--hill-mauve) 36%,
      var(--hill-violet) 55%,
      var(--hill-blue) 72%,
      var(--hill-deep) 100%
    );
  }
  .volume {
    position: absolute;
    left: 0;
    top: 796px;
    width: 100%;
    text-align: center;
    font-family: "Caveat", cursive;
    font-weight: 500;
    font-size: 46px;
    line-height: 1;
    color: var(--volume-mark);
  }
</style>
</head>
<body>
  <main class="canvas">
    <section class="wine-label">
      <header class="label-header">
        <h1 class="brand-name">LOREM IPSUM</h1>
        <p class="tagline">Contrary to popular belief</p>
      </header>
      <div class="landscape" role="img" aria-label="Painted layers of rolling hills fading from soft pink through mauve to deep blue"></div>
      <p class="volume">1l</p>
    </section>
  </main>
</body>
</html>
```